Slides for industrial furniture site

I am looking for three slides (1400x530) that will go on my homepage. All slides need to be simple and a projection of the goods i am selling.
The slides need to be up there in the design trends for 2014.
I prefer:
- One large photo in each slide, maybe faded with a product in the front.
- Some example text in different fonts.
- light coloured slides. That go well in white oriented site.
- pictures may include these products: https://www.findora-example.nl/search?q=morvane+lights
AND:
https://www.findora-example.nl/search?q=vintage+theatre+light
OR:
https://www.findora-example.nl/search?q=vintage+stools
OR:
https://www.findora-example.nl/search?q=brevak+chair#q=original%20brevak%20chair
Maybe one slide with an interior like this:
https://www.findora-example.nl/search?q=industrial+interiors
Just let me see your creations and take into account the above.
For some examples:
http://quietmarsh-example.co/
http://pixelhof-example.at/en/
https://www.fernandlamp-example.com/
http://www.ulvastudio-example.com/
http://quillbarrow-example.ca/en/
http://skinforge-example.com/
For some theory (sorry if this is offensive ;-):
http://www.deckvault-example.net/plumo/font-pairing-slides
http://www.deckvault-example.net/brightmill2014/web-design-trends-2014
http://www.deckvault-example.net/tobyrand/how-to-create-great-slides-for-presentations
I hope you can create great slides for me!
Thnx
Reason: Hi designers. I am still looking for the perfect three lsides. Could you please make a few more.
Greetings,
Harlem
Reason: Sorry designers.
I am waiting for some designs from specific designers.
Industrial

```html
<!DOCTYPE html>
<html lang="en">
<head>
<meta charset="utf-8">
<title>Industrial Furniture – Homepage Slides</title>
<link rel="stylesheet" href="https://fonts.googleapis.com/css2?family=Varela+Round&family=Nunito:wght@300&family=Open+Sans:wght@400;700&display=swap">
<style>
  :root {
    --page: #ffffff;
    --ink-light: #ffffff;
    --ink-soft: #eef0f2;
    --accent: #1493d3;
    --accent-dark: #0f3a57;
    --accent-line: #1c6c9e;
    --slide-dark: #1c1c1d;
    --slide-mid: #3a3836;
    --brick: #5b3f32;
    --mint: #8fd9d2;
    --chair-white: #d9dadc;
    --chair-pink: #d58aa6;
    --chair-red: #e8504a;
    --dot-idle: #b9b9b9;
  }
  * { box-sizing: border-box; margin: 0; padding: 0; }
  html, body { width: 1026px; height: 1200px; overflow: hidden; background: var(--page); }
  .slides { position: relative; width: 1026px; height: 1200px; }
  .slide { position: absolute; left: 0; width: 1026px; height: 388px; overflow: hidden; color: var(--ink-light); font-family: "Open Sans", sans-serif; }
  .slide--one { top: 0; }
  .slide--two { top: 406px; }
  .slide--three { top: 812px; }

  .backdrop { position: absolute; inset: 0; }
  .slide--one .backdrop {
    background:
      radial-gradient(ellipse 40% 45% at 58% 50%, rgba(120,95,70,.55), transparent 70%),
      radial-gradient(ellipse 30% 60% at 90% 30%, rgba(140,140,140,.45), transparent 70%),
      linear-gradient(180deg, #4a4a4a 0%, #2d2c2b 45%, #141414 100%);
  }
  .slide--two .backdrop {
    background:
      radial-gradient(ellipse 25% 40% at 18% 30%, rgba(120,75,55,.7), transparent 70%),
      radial-gradient(ellipse 20% 35% at 72% 35%, rgba(130,90,65,.6), transparent 70%),
      radial-gradient(ellipse 18% 25% at 85% 25%, rgba(150,150,150,.35), transparent 70%),
      linear-gradient(180deg, #3c322e 0%, #262221 55%, #121212 100%);
  }
  .slide--three .backdrop {
    background:
      radial-gradient(ellipse 25% 45% at 12% 30%, rgba(140,140,140,.5), transparent 70%),
      radial-gradient(ellipse 30% 40% at 70% 20%, rgba(130,95,70,.6), transparent 70%),
      radial-gradient(ellipse 25% 30% at 35% 60%, rgba(110,85,65,.45), transparent 70%),
      linear-gradient(180deg, #3b3835 0%, #2a2725 50%, #1a1817 100%);
  }

  .product { position: absolute; border-radius: 28% 28% 10% 10% / 20% 20% 6% 6%; }
  .product--mint { background: radial-gradient(ellipse at 50% 40%, var(--mint), rgba(143,217,210,.25) 75%, transparent); }
  .product--white { background: radial-gradient(ellipse at 50% 40%, var(--chair-white), rgba(217,218,220,.25) 75%, transparent); }
  .product--pink { background: radial-gradient(ellipse at 50% 40%, var(--chair-pink), rgba(213,138,166,.25) 75%, transparent); }
  .product--blush { background: radial-gradient(ellipse at 50% 40%, #e6c9cc, rgba(230,201,204,.25) 75%, transparent); }
  .product--red { background: radial-gradient(ellipse at 50% 40%, var(--chair-red), rgba(232,80,74,.25) 75%, transparent); }

  .headline { position: absolute; font-family: "Varela Round", "Nunito", sans-serif; font-weight: 400; line-height: 1; white-space: nowrap; }
  .lede { position: absolute; font-size: 14.5px; line-height: 18px; color: var(--ink-soft); }

  /* slide one */
  .slide--one .headline { left: 0; width: 1026px; top: 68px; text-align: center; font-size: 32px; }
  .slide--one .lede { left: 0; width: 1026px; top: 111px; text-align: center; }
  .learn-more { position: absolute; left: 886px; top: 332px; width: 118px; height: 30px; }
  .learn-more span { position: absolute; left: 0; top: 0; width: 96px; height: 30px; line-height: 30px; text-align: center; font-weight: 700; font-size: 12px; color: var(--ink-light); letter-spacing: .2px; }
  .hex-nav { position: absolute; left: 963px; top: 21px; }

  /* slide two */
  .slide--two .headline { left: 0; width: 1026px; top: 126px; text-align: center; font-size: 34px; }
  .slide--two .lede { left: 0; width: 1026px; top: 168px; text-align: center; }
  .cta-outline { position: absolute; left: 451px; top: 207px; width: 124px; height: 35px; border: 1px solid var(--accent-line); border-radius: 2px; background: rgba(15,58,87,.25); color: var(--accent); font-size: 12px; line-height: 33px; text-align: center; }
  .progress { position: absolute; left: 14px; top: 366px; display: flex; gap: 1px; }
  .progress i { display: block; width: 29px; height: 3px; background: rgba(180,180,180,.6); }
  .progress i.is-active { background: var(--ink-light); }

  /* slide three */
  .slide--three .headline { right: 440px; top: 122px; text-align: right; font-size: 31px; line-height: 39px; letter-spacing: .5px; text-transform: uppercase; }
  .slide--three .lede { right: 440px; top: 203px; text-align: right; }
  .cta-solid { position: absolute; left: 470px; top: 257px; width: 117px; height: 37px; background: var(--accent); color: var(--ink-light); font-size: 13px; line-height: 37px; text-align: center; }
  .dots { position: absolute; left: 946px; top: 347px; display: flex; gap: 3px; }
  .dots i { display: block; width: 12px; height: 12px; border-radius: 50%; background: var(--dot-idle); }
  .dots i.is-active { background: var(--ink-light); }
</style>
</head>
<body>
<main class="slides">

  <section class="slide slide--one">
    <div class="backdrop" role="img" aria-label="Blurred dark industrial kitchen and dining interior"></div>
    <div class="product product--mint" style="left:344px;top:200px;width:94px;height:140px" role="img" aria-label="Mint metal armchair"></div>
    <div class="product product--white" style="left:474px;top:200px;width:96px;height:140px" role="img" aria-label="White metal armchair"></div>
    <div class="product product--pink" style="left:595px;top:200px;width:97px;height:140px" role="img" aria-label="Pink metal armchair"></div>
    <h2 class="headline">Lorem ipsum dolor sit amet, consectetur</h2>
    <p class="lede">Sed ut perspiciatis unde omnis iste natus error sit voluptatem accusantium&nbsp; eaque ipsa<br>inventore veritatis et quasi architecto beatae</p>
    <a class="learn-more">
      <svg width="118" height="30" viewBox="0 0 118 30"><path d="M0 0H102L118 15L102 30H0Z" fill="var(--accent)"/></svg>
      <span>LEARN MORE</span>
    </a>
    <svg class="hex-nav" width="40" height="14" viewBox="0 0 40 14">
      <path d="M6 1L11.5 4V10L6 13L0.5 10V4Z" fill="#fff"/>
      <path d="M19 1.5L24 4.3V9.7L19 12.5L14 9.7V4.3Z" fill="none" stroke="#fff" stroke-width="1.3"/>
      <path d="M32 1.5L37 4.3V9.7L32 12.5L27 9.7V4.3Z" fill="none" stroke="#fff" stroke-width="1.3"/>
    </svg>
  </section>

  <section class="slide slide--two">
    <div class="backdrop" role="img" aria-label="Blurred industrial loft with brick walls and staircase"></div>
    <div class="product product--white" style="left:78px;top:77px;width:170px;height:247px" role="img" aria-label="White metal armchair"></div>
    <div class="product product--blush" style="left:764px;top:77px;width:170px;height:247px" role="img" aria-label="Blush pink metal armchair"></div>
    <h2 class="headline">Lorem ipsum dolor sit consectetur</h2>
    <p class="lede">Sed ut perspiciatis unde omnis iste natus error sit voluptatem.</p>
    <a class="cta-outline">CALL TO ACTION</a>
    <div class="progress"><i class="is-active"></i><i></i><i></i></div>
  </section>

  <section class="slide slide--three">
    <div class="backdrop" role="img" aria-label="Blurred industrial interior with wooden beams and stairs"></div>
    <div class="product product--red" style="left:662px;top:44px;width:222px;height:324px" role="img" aria-label="Red metal armchair"></div>
    <h2 class="headline">Lorem ipsum dolor sit<br>amet, consectetur</h2>
    <p class="lede">Sed ut perspiciatis unde omnis iste natus error<br>sit voluptatem accusantium&nbsp; eaque ipsa</p>
    <a class="cta-solid">Call to Action</a>
    <div class="dots"><i class="is-active"></i><i></i><i></i></div>
  </section>

</main>
</body>
</html>
```